Standard logo business card

We are seeking a solid, somewhat understated professional design. We are a tech company. We like fonts similar to Aptifer Slab. Front side will be white with the contact information and a small version of our primary (Light background) logo.

(We have three people so we will have three names and titles)

Back side will hold our reverse logo on dark background along with the tagline:

"Intelligent annotation solutions for complex data"

Target Market(s)

Professionals, Tech

Industry/Entity Type

Business

Contact Information for Business Card

Name
Title

Phone
Email
City, State
Website

[We will email leading designer specific contact information)

Font styles to use
Serif

Requirements
Must have
• Colors are:
• Orange RGB 245,92,23
• Blue RGB 3,34,56
Nice to have
• We like a split with the Name and Title on the right and then contact details (below) on the left.

```html
<!DOCTYPE html>
<html lang="en">
<head>
<meta charset="utf-8">
<title>Norvanta – Business Card</title>
<link rel="stylesheet" href="https://fonts.googleapis.com/css2?family=Aleo:wght@300;400&family=Open+Sans:wght@400;700&display=swap">
<style>
  :root {
    --orange: rgb(245, 92, 23);
    --blue: rgb(3, 34, 56);
    --white: #ffffff;
    --page: #ffffff;
  }
  * { box-sizing: border-box; margin: 0; padding: 0; }
  html, body {
    width: 1200px;
    height: 1165px;
    overflow: hidden;
    background: var(--page);
  }
  .canvas {
    position: relative;
    width: 1200px;
    height: 1165px;
  }
  .card {
    position: absolute;
    left: 18px;
    width: 1121px;
    height: 483px;
    box-shadow: 14px 14px 18px rgba(0, 0, 0, 0.35);
  }
  .card--front {
    top: 18px;
    background: var(--white);
  }
  .card--back {
    top: 620px;
    background: var(--blue);
  }

  /* Wordmark */
  .wordmark {
    position: absolute;
    display: flex;
    align-items: center;
    gap: 22px;
  }
  .wordmark__square {
    width: 96px;
    height: 96px;
    background: var(--orange);
    flex: none;
  }
  .wordmark__name {
    font-family: "Open Sans", Arial, sans-serif;
    font-weight: 700;
    font-size: 118px;
    line-height: 1;
    letter-spacing: -3px;
  }
  .card--front .wordmark {
    left: 0;
    right: 0;
    top: 50px;
    justify-content: center;
  }
  .card--front .wordmark__name { color: var(--blue); }
  .card--back .wordmark {
    left: 43px;
    top: 40px;
  }
  .card--back .wordmark__name { color: var(--white); }

  /* Contact band */
  .contact-band {
    position: absolute;
    left: 28px;
    top: 328px;
    width: 1063px;
    height: 133px;
    background: var(--blue);
  }
  .contact-item {
    position: absolute;
    display: flex;
    align-items: center;
    height: 40px;
    font-family: "Open Sans", Arial, sans-serif;
    font-size: 26px;
    color: var(--white);
  }
  .contact-item__icon {
    width: 70px;
    height: 40px;
    flex: none;
  }
  .contact-item__label { margin-left: 56px; }
  .contact-item--phone   { left: 24px;  top: 14px; }
  .contact-item--office  { left: 24px;  top: 71px; }
  .contact-item--website { left: 615px; top: 14px; }
  .contact-item--email   { left: 615px; top: 71px; }

  /* Back side */
  .tagline {
    position: absolute;
    left: 36px;
    top: 200px;
    font-family: "Aleo", Georgia, serif;
    font-weight: 300;
    font-size: 35px;
    color: var(--white);
    white-space: nowrap;
  }
  .back-rule {
    position: absolute;
    left: 28px;
    top: 436px;
    width: 1063px;
    height: 22px;
    background: var(--white);
  }
</style>
</head>
<body>
<main class="canvas">

  <section class="card card--front" aria-label="Business card front">
    <div class="wordmark">
      <span class="wordmark__square"></span>
      <span class="wordmark__name">Norvanta</span>
    </div>

    <div class="contact-band">
      <div class="contact-item contact-item--phone">
        <svg class="contact-item__icon" viewBox="0 0 70 40" aria-hidden="true">
          <path d="M6 22 L35 6 L64 22 L58 22 L35 10 L12 22 Z" fill="#fff"/>
          <path d="M17 22 L35 13 L53 22 L53 32 L17 32 Z" fill="#fff"/>
        </svg>
        <span class="contact-item__label" style="margin-left:16px">Phone number:</span>
      </div>
      <div class="contact-item contact-item--office">
        <svg class="contact-item__icon" viewBox="0 0 70 40" aria-hidden="true">
          <path d="M8 30 C6 26 10 22 14 24 L20 27 C30 20 40 14 52 10 L50 4 C54 1 60 2 62 6 C64 10 60 14 56 14 C44 20 32 28 22 34 C18 37 10 34 8 30 Z" fill="#fff"/>
        </svg>
        <span class="contact-item__label" style="margin-left:16px">Office location:</span>
      </div>
      <div class="contact-item contact-item--website">
        <svg class="contact-item__icon" viewBox="0 0 70 50" aria-hidden="true" style="height:50px">
          <rect x="2" y="2" width="66" height="46" fill="none" stroke="#fff" stroke-width="2"/>
          <circle cx="35" cy="25" r="17" fill="none" stroke="#fff" stroke-width="2"/>
          <ellipse cx="35" cy="25" rx="8" ry="17" fill="none" stroke="#fff" stroke-width="2"/>
          <line x1="35" y1="8" x2="35" y2="42" stroke="#fff" stroke-width="2"/>
          <line x1="18" y1="25" x2="52" y2="25" stroke="#fff" stroke-width="2"/>
          <line x1="21" y1="17" x2="49" y2="17" stroke="#fff" stroke-width="2"/>
          <line x1="21" y1="33" x2="49" y2="33" stroke="#fff" stroke-width="2"/>
        </svg>
        <span class="contact-item__label">Website:</span>
      </div>
      <div class="contact-item contact-item--email">
        <svg class="contact-item__icon" viewBox="0 0 70 40" aria-hidden="true">
          <rect x="4" y="6" width="62" height="30" rx="3" fill="#fff"/>
          <path d="M6 8 L35 26 L64 8" fill="none" stroke="var(--blue)" stroke-width="2.5"/>
          <path d="M6 34 L27 21 M64 34 L43 21" fill="none" stroke="var(--blue)" stroke-width="2"/>
        </svg>
        <span class="contact-item__label">Email address:</span>
      </div>
    </div>
  </section>

  <section class="card card--back" aria-label="Business card back">
    <div class="wordmark">
      <span class="wordmark__square"></span>
      <span class="wordmark__name">Norvanta</span>
    </div>
    <p class="tagline">"Intelligent annotation solutions for complex data"</p>
    <div class="back-rule"></div>
  </section>

</main>
</body>
</html>
```